I need a luxury/high-end real estate looking website for my Vending business

Hello & thank you in advance for your time spent on this project.

I have a vending business (Amber Crest Vending Services) based here in downtown Coral Harbor & my clients are high-end/luxury buildings throughout the area.
We offer free placement of 5 vending machine options (snacks, drinks, laundry products, healthy options or combo machine) to high traffic locations.

The goal of this website is to be a lead generator. So having an inquiry form on the top of the page is key.

Aesthetically, I want the website to feel like a high-end commercial real estate website. We service luxury buildings, so I want that look of the downtown skyline mixed in with the vending machine images throughout the site.

On the main page, it would be :
*the inquiry form (name of location, # of machines, machine option, contact info)
*What we do section - vending machine placement, bi-weekly or monthly refill service & ongoing customer support.
*5 vending machine options section - (with clickable images to see what all products you can have the machine filled with)
*reviews section
*social feed or blog post section
*about us section
then of course the contact info etc at the bottom of page

For the question ''how many pages do you need designed'', I answered 5+, which is in reference to the main page outlined above plus the 5 clickable images that takes you to the product options. I'm assuming the clickable images would be pages on their own.

Target Market(s)

High traffic businesses & residences in downtown Coral Harbor

Industry/Entity Type

Vending Machines

Coding

Coded - Design and coding required

Number of Pages Required

5+ page

Requirements
Must have
• Inquiry form
Nice to have
• To have a feel of a luxury/high-end commercial real estate website

```html
<!DOCTYPE html>
<html lang="en">
<head>
<meta charset="utf-8">
<title>Amber Crest Vending Services</title>
<link href="https://fonts.googleapis.com/css2?family=Lato:wght@400;700;900&family=Poppins:wght@400;500;600&display=swap" rel="stylesheet">
<style>
:root{
  --cyan:#00b7dc;
  --cyan-dark:#0096c2;
  --blue:#0a72e6;
  --navy:#0e5f78;
  --ink:#111;
  --text:#333;
  --muted:#666;
  --light:#f0f0f0;
  --white:#fff;
  --black:#000;
  --star:#f5b400;
}
*{box-sizing:border-box;margin:0;padding:0}
html,body{width:1200px;height:4059px;overflow:hidden}
body{font-family:"Lato",sans-serif;color:var(--text);background:var(--white);position:relative}
section,header,nav,footer{position:absolute;left:0;width:1200px}
.abs{position:absolute}
.eyebrow{font-family:"Poppins",sans-serif;font-weight:600;font-size:16px;letter-spacing:4px;color:var(--blue);text-transform:uppercase}
.title{font-weight:700;font-size:35px;color:var(--ink)}
.center{left:0;width:1200px;text-align:center}
.photo{position:absolute}

/* top nav */
.topnav{top:0;height:68px;background:var(--cyan)}
.topnav a{position:absolute;top:23px;font-size:16px;color:var(--white);text-decoration:none;transform:translateX(-50%)}
.topnav a.active{font-weight:700;text-decoration:underline}

/* header */
.masthead{top:68px;height:112px;background:var(--white)}
.brand{left:110px;top:24px;display:flex;align-items:center;gap:14px}
.brand-mark{width:42px;height:66px;background:var(--blue)}
.brand-name{font-weight:700;font-size:31px;line-height:1.1;color:var(--ink)}
.brand-sub{font-weight:700;font-size:20px;letter-spacing:7px;color:var(--cyan);display:block}
.call{left:737px;top:12px;font-weight:700;font-size:25px;color:var(--ink)}
.call b{font-weight:700;font-size:21px}
.btn-outline{position:absolute;height:43px;border:3px solid var(--cyan);padding:3px}
.btn-outline span{display:flex;height:100%;align-items:center;justify-content:center;background:var(--cyan);color:var(--white);font-weight:700;font-size:14px}

/* hero */
.hero{top:180px;height:551px;background:linear-gradient(135deg,#1ab7d8,#0aa2cc 60%,#1ab7d8);overflow:hidden}
.hero-photo{left:0;top:0;width:700px;height:551px;background:linear-gradient(110deg,#5d6670,#a8a49c 40%,#d9d4cb 70%,#efece6);clip-path:polygon(0 0,545px 0,700px 551px,0 551px)}
.hero-welcome{right:110px;top:32px;text-align:right;color:var(--white)}
.hero-welcome .small{font-weight:700;font-size:23px}
.hero-welcome .big{font-weight:700;font-size:35px;margin-top:4px}
.btn-white{position:absolute;border:3px solid var(--white);padding:3px}
.btn-white span{display:flex;height:100%;align-items:center;justify-content:center;background:var(--white);color:var(--blue);font-weight:700;font-size:14px}
.inquiry{left:723px;top:189px;width:367px;height:300px;background:var(--navy);border:3px solid var(--cyan)}
.inquiry h2{text-align:center;color:var(--white);font-weight:700;font-size:21px;margin-top:16px}
.field{position:absolute;height:41px;border:1px solid #9ec9d6;color:var(--white);font-size:12px;padding:0 8px;display:flex;align-items:center;justify-content:space-between}
.field svg{width:10px;height:6px}
.submit{left:830px;top:460px;width:155px;height:47px;background:var(--white);color:var(--navy);font-weight:700;font-size:16px;display:flex;align-items:center;justify-content:center}

/* about */
.about{top:731px;height:504px;background:var(--white)}
.about .eyebrow{left:110px;top:72px}
.about .title{left:110px;top:102px;font-size:31px;width:560px;white-space:nowrap}
.about p{position:absolute;left:110px;width:520px;font-size:14.5px;line-height:26px;color:var(--text)}
.about-accent{left:800px;top:164px;width:400px;height:340px;background:var(--blue)}
.about-photo{left:687px;top:85px;width:403px;height:346px;border:3px solid var(--cyan);background:linear-gradient(160deg,#6fb3e8,#3f9fb8 45%,#1f8f8f 70%,#2a7a8c);box-shadow:0 6px 20px rgba(0,0,0,.2)}

/* categories */
.categories{top:1235px;height:567px;background:linear-gradient(180deg,#1bb6da,#0aa6d2)}
.categories .eyebrow{top:48px;color:var(--white)}
.categories .title{top:74px;color:var(--white)}
.cat-card{position:absolute;top:143px;width:220px;height:336px;background:var(--white);border:2px solid var(--white)}
.cat-card .photo{left:0;top:0;width:216px;height:300px}
.cat-card .label{position:absolute;left:28px;right:0;bottom:0;height:54px;background:var(--white);display:flex;align-items:center;justify-content:center;font-size:19px;font-weight:700;color:var(--ink)}
.arrow{position:absolute;top:297px;width:34px;height:34px;border-radius:50%;background:var(--white);display:flex;align-items:center;justify-content:center}

/* testimonials */
.testimonials{top:1802px;height:554px;background:var(--white)}
.testimonials .eyebrow{top:58px}
.testimonials .title{top:88px}
.t-card{position:absolute;left:110px;width:339px;height:97px;background:var(--light);display:flex;align-items:center;padding-left:22px;gap:18px}
.t-card.active{background:var(--white);border:2px solid var(--blue);box-shadow:0 4px 14px rgba(0,0,0,.1)}
.avatar{width:64px;height:64px;border-radius:50%;background:linear-gradient(135deg,#b9a89a,#6d5a4e)}
.t-name{font-weight:700;font-size:22px;color:var(--ink)}
.t-card.active .t-name{color:var(--blue);text-transform:uppercase}
.t-role{font-family:"Poppins",sans-serif;font-size:11px;font-weight:500;color:var(--ink);margin-top:4px}
.quote{left:558px;top:150px;width:540px}
.quote-name{font-weight:700;font-size:24px;color:var(--ink)}
.quote-name small{font-family:"Poppins",sans-serif;font-weight:500;font-size:11px;color:var(--muted);margin-left:8px}
.stars{color:var(--star);font-size:20px;letter-spacing:1px;margin-top:8px}
.quote p{font-size:14.5px;line-height:31px;color:var(--text);margin-top:14px}
.quote .sign{font-weight:700;font-size:16px;color:var(--blue);margin-top:10px}

/* services */
.services{top:2356px;height:581px;background:linear-gradient(180deg,#0a72e6,#0c6ad8 70%,#0a5fc4)}
.services .eyebrow{top:56px;color:var(--white)}
.services .title{top:84px;color:var(--white)}
.svc-card{position:absolute;top:142px;width:296px;height:368px}
.svc-card .photo{left:0;top:0;width:296px;height:310px}
.svc-card .label{position:absolute;left:0;right:0;bottom:0;height:80px;background:var(--white);display:flex;align-items:center;justify-content:center;text-align:center;font-size:19px;line-height:28px;color:var(--ink)}
.svc-card .label::before{content:"";position:absolute;left:20px;right:20px;top:-18px;height:18px;background:var(--white)}

/* blog */
.blog{top:2937px;height:662px;background:var(--white)}
.blog .eyebrow{top:63px}
.blog .title{top:93px}
.post{position:absolute;top:145px;width:292px;height:454px}
.post .photo{left:0;top:0;width:292px;height:240px}
.post .body{position:absolute;left:13px;right:13px;top:190px;bottom:14px;background:var(--white);text-align:center;padding:20px 18px 0;box-shadow:0 6px 16px rgba(0,0,0,.07)}
.post.featured{background:var(--blue)}
.post h3{font-weight:700;font-size:19px;color:var(--ink)}
.post .date{font-family:"Poppins",sans-serif;font-size:11px;color:var(--ink);margin-top:6px}
.post.featured .date{color:var(--blue)}
.post p{font-size:14.5px;line-height:26px;color:var(--muted);margin-top:6px}
.post .more{margin-top:12px;font-weight:700;font-size:16px;color:var(--ink);text-decoration:underline;display:flex;align-items:center;justify-content:center;gap:14px}
.post.featured .more{color:var(--blue)}

/* footer */
.site-footer{top:3599px;height:460px;background:var(--black);color:var(--white)}
.f-brand{left:110px;top:95px;display:flex;align-items:center;gap:12px}
.f-brand .brand-mark{width:36px;height:58px;background:var(--white)}
.f-brand .brand-name{color:var(--white);font-size:26px}
.f-brand .brand-sub{color:var(--white);font-size:17px;letter-spacing:6px}
.socials{left:110px;top:194px;display:flex;gap:16px}
.socials span{width:34px;height:34px;background:var(--blue)}
.f-head{position:absolute;top:92px;font-weight:700;font-size:20px}
.f-text{font-size:13px;line-height:25px}
.f-input{left:446px;top:211px;width:229px;height:45px;background:var(--white);color:#888;font-size:12px;padding-left:18px;display:flex;align-items:center}
.f-sub{left:446px;top:258px;width:186px;height:55px;background:var(--blue);font-weight:700;font-size:16px;padding-left:18px;display:flex;align-items:center}
.contact-row{position:absolute;left:701px;display:flex;align-items:flex-start;gap:13px;font-size:14.5px;line-height:26px}
.contact-row .ic{width:34px;height:34px;background:var(--blue);display:flex;align-items:center;justify-content:center;flex:none}
.links{left:972px;top:140px}
.links li{list-style:none;font-size:14.5px;height:34px;display:flex;align-items:center;gap:12px}
.f-rule{left:110px;top:376px;width:980px;height:2px;background:#555}
.copy{top:413px;font-size:13px}
</style>
</head>
<body>

<nav class="topnav">
  <a class="active" style="left:223px" href="#">Home</a>
  <a style="left:364px" href="#">About Us</a>
  <a style="left:520px" href="#">Services</a>
  <a style="left:668px" href="#">Gallery</a>
  <a style="left:828px" href="#">Testimonials</a>
  <a style="left:984px" href="#">Blog</a>
</nav>

<header class="masthead">
  <div class="brand abs">
    <span class="brand-mark"></span>
    <div class="brand-name">Amber Crest Vending<span class="brand-sub">SERVICES</span></div>
  </div>
  <div class="call abs"><b>CALL NOW:</b> +1 305 555 0142</div>
  <div class="btn-outline" style="left:715px;top:49px;width:192px"><span>SCHEDULE SERVICE</span></div>
  <div class="btn-outline" style="left:945px;top:49px;width:142px"><span>CONTACT US</span></div>
</header>

<section class="hero">
  <div class="photo hero-photo" role="img" aria-label="Woman with a coffee cup choosing an item on a vending machine keypad"></div>
  <div class="hero-welcome abs">
    <div class="small">WELCOME TO</div>
    <div class="big">Amber Crest Vending Services</div>
  </div>
  <div class="btn-white" style="left:945px;top:120px;width:140px;height:43px"><span>GET STARTED</span></div>
  <form class="inquiry abs">
    <h2>SEND US A MESSAGE</h2>
    <div class="field" style="left:15px;top:53px;width:331px">Name of location <svg viewBox="0 0 10 6"><path d="M0 0h10L5 6z" fill="#fff"/></svg></div>
    <div class="field" style="left:15px;top:105px;width:331px">No of machines <svg viewBox="0 0 10 6"><path d="M0 0h10L5 6z" fill="#fff"/></svg></div>
    <div class="field" style="left:15px;top:157px;width:158px">Machine Option <svg viewBox="0 0 10 6"><path d="M0 0h10L5 6z" fill="#fff"/></svg></div>
    <div class="field" style="left:189px;top:157px;width:157px">Name</div>
    <div class="field" style="left:15px;top:209px;width:158px">Email</div>
    <div class="field" style="left:189px;top:209px;width:157px">Phone Number</div>
  </form>
  <div class="submit abs">SUBMIT</div>
</section>

<section class="about">
  <div class="about-accent abs"></div>
  <div class="eyebrow abs">WHO WE ARE</div>
  <h2 class="title abs">About Amber Crest Vending Services</h2>
  <p style="top:143px">Nam libero tempore, cum soluta nobis est eligendi optio cumque nihil impedit quo minus id quod maxime placeat facere possimus, omnis voluptas assumenda est, omnis dolor repellendus. Temporibus autem quibusdam et aut officiis debitis aut rerum necessitatibus saepe eveniet ut et voluptates repudiandae sint et molestiae non recusandae.</p>
  <p style="top:297px">Itaque earum rerum hic tenetur a sapiente delectus, ut aut reiciendis voluptatibus maiores alias consequatur aut perferendis doloribus asperiores repellat.</p>
  <div class="btn-outline" style="left:110px;top:390px;width:144px;height:48px"><span>READ MORE</span></div>
  <div class="photo about-photo" role="img" aria-label="Aerial view of high-rise towers beside a marina"></div>
</section>

<section class="categories">
  <div class="eyebrow abs center">VENDING</div>
  <h2 class="title abs center">Our Categories</h2>
  <div class="arrow" style="left:33px"><svg width="14" height="14" viewBox="0 0 14 14"><path d="M9 2 4 7l5 5" stroke="#0a72e6" stroke-width="2.4" fill="none"/></svg></div>
  <div class="arrow" style="left:1130px"><svg width="14" height="14" viewBox="0 0 14 14"><path d="M5 2l5 5-5 5" stroke="#0a72e6" stroke-width="2.4" fill="none"/></svg></div>
  <div class="cat-card" style="left:110px"><div class="photo" role="img" aria-label="Woman selecting snacks at a vending machine" style="background:linear-gradient(160deg,#2a3f8a,#8a7f96 50%,#d9c9b6)"></div><div class="label">Snacks</div></div>
  <div class="cat-card" style="left:364px"><div class="photo" role="img" aria-label="Hand pressing the keypad of a drinks machine" style="background:linear-gradient(90deg,#9fb6c7,#4f6070 45%,#1c2228)"></div><div class="label">Drinks</div></div>
  <div class="cat-card" style="left:616px"><div class="photo" role="img" aria-label="Hand turning the coin knob of a red laundry products dispenser" style="background:linear-gradient(150deg,#e06a52,#c8473a 55%,#a8a09a)"></div><div class="label">Laundry Products</div></div>
  <div class="cat-card" style="left:868px"><div class="photo" role="img" aria-label="Row of healthy option vending machines" style="background:linear-gradient(180deg,#b8c2cc,#3a4048 50%,#8a9098)"></div><div class="label">Healthy</div></div>
</section>

<section class="testimonials">
  <div class="eyebrow abs center">TESTIMONIALS</div>
  <h2 class="title abs center">What Customer Says</h2>
  <div class="t-card" style="top:156px"><span class="avatar" role="img" aria-label="Portrait of the customer"></span><div><div class="t-name">Nora Whitfield</div><div class="t-role">Senior Manager, United States</div></div></div>
  <div class="t-card active" style="top:274px"><span class="avatar" role="img" aria-label="Portrait of the customer"></span><div><div class="t-name">Dario Velasco</div><div class="t-role">Assistant Manager, United States</div></div></div>
  <div class="t-card" style="top:405px"><span class="avatar" role="img" aria-label="Portrait of the customer"></span><div><div class="t-name">Nora Whitfield</div><div class="t-role">Senior Manager, United States</div></div></div>
  <div class="quote abs">
    <div class="quote-name">Dario Velasco<small>(Assistant Manager, United States)</small></div>
    <div class="stars">★★★★★</div>
    <p>Temporibus autem quibusdam et aut officiis debitis aut rerum necessitatibus saepe eveniet ut et voluptates repudiandae sint et molestiae non recusandae.</p>
    <p style="margin-top:31px">Itaque earum rerum hic tenetur a sapiente delectus, ut aut reiciendis voluptatibus maiut officiis debitis aut rerum necessitatibus saepe eveniet ut a sapiente delectus, ut aut reiciendis voluptatibusores alias consequatur aut perferendis doloribus asperiores repellat.</p>
    <div class="sign">Thanks, Amber Crest Vending Services</div>
  </div>
</section>

<section class="services">
  <div class="eyebrow abs center">SERVICES</div>
  <h2 class="title abs center">What We Do</h2>
  <div class="svc-card" style="left:110px"><div class="photo" role="img" aria-label="Stocked snack and drinks vending machine" style="background:linear-gradient(90deg,#3d8c3a,#c0b070 40%,#7aa0c0 70%,#4a7a3a)"></div><div class="label">Vending Machine<br>Placement</div></div>
  <div class="svc-card" style="left:451px"><div class="photo" role="img" aria-label="Technician refilling a coffee vending machine" style="background:linear-gradient(150deg,#d8dadc,#8a4040 55%,#2a3040)"></div><div class="label">Bi-weekly or Monthly<br>Refill Service</div></div>
  <div class="svc-card" style="left:792px"><div class="photo" role="img" aria-label="Hand touching a glowing five-star satisfaction icon" style="background:radial-gradient(circle at 45% 40%,#5fc0e8,#1a5a8a 55%,#0a2a4a)"></div><div class="label">Ongoing Customer<br>Support</div></div>
</section>

<section class="blog">
  <div class="eyebrow abs center">BLOG</div>
  <h2 class="title abs center">Latest News</h2>
  <article class="post" style="left:110px">
    <div class="photo" role="img" aria-label="Woman choosing a snack at a vending machine" style="background:linear-gradient(160deg,#2a3f8a,#8a7f96 50%,#d9c9b6)"></div>
    <div class="body"><h3>Finibus Bonorum</h3><div class="date">Feb 04, 2023</div><p>Quis autem vel eum iure reprehenderit qui in ea voltate velit esse quam nihil molestiae conseatur, &nbsp;quo voluptas velit pariatur.</p><div class="more">Read More <svg width="16" height="16" viewBox="0 0 16 16"><circle cx="8" cy="8" r="8" fill="#111"/><path d="M5 8h6M8 5l3 3-3 3" stroke="#fff" stroke-width="1.6" fill="none"/></svg></div></div>
  </article>
  <article class="post featured" style="left:452px">
    <div class="photo" role="img" aria-label="Man smiling while pointing to a vending machine" style="background:linear-gradient(150deg,#e8e6e2,#b0a89e 50%,#3a302a)"></div>
    <div class="body"><h3>Volupta Accusanti</h3><div class="date">Mar 23, 2023</div><p>Excepteur sint occaecat cupidatat non proident, sunt in culpa qui officia nostrud exercitation ullamco laboris nisi deserunt tenetur a sapiente delectus id &nbsp;laborum.</p><div class="more">Read More <svg width="16" height="16" viewBox="0 0 16 16"><circle cx="8" cy="8" r="8" fill="#0a72e6"/><path d="M5 8h6M8 5l3 3-3 3" stroke="#fff" stroke-width="1.6" fill="none"/></svg></div></div>
  </article>
  <article class="post" style="left:795px">
    <div class="photo" role="img" aria-label="Woman in front of a drinks vending machine" style="background:linear-gradient(150deg,#d8e0e6,#b85a2a 55%,#3a2a22)"></div>
    <div class="body"><h3>Tempor Incididunt</h3><div class="date">Mar 17, 2023</div><p>Quis autem vel eum iure reprehenderit qui in ea voltate velit esse quam nihil molestiae conseatur, &nbsp;quo voluptas velit pariatur.</p><div class="more">Read More <svg width="16" height="16" viewBox="0 0 16 16"><circle cx="8" cy="8" r="8" fill="#111"/><path d="M5 8h6M8 5l3 3-3 3" stroke="#fff" stroke-width="1.6" fill="none"/></svg></div></div>
  </article>
</section>

<footer class="site-footer">
  <div class="f-brand abs">
    <span class="brand-mark"></span>
    <div class="brand-name">Amber Crest Vending<span class="brand-sub">SERVICES</span></div>
  </div>
  <div class="socials abs"><span></span><span></span><span></span><span></span></div>

  <div class="f-head" style="left:446px">Subscribe Us</div>
  <p class="f-text abs" style="left:446px;top:137px;width:215px">Itaque earum rerum hic tenetur a voluptatibus maiores aliasr</p>
  <div class="f-input abs">Enter The Email</div>
  <div class="f-sub abs">Subscribe</div>

  <div class="f-head" style="left:701px">Contact Us</div>
  <div class="contact-row" style="top:140px"><span class="ic"><svg width="14" height="18" viewBox="0 0 14 18"><path d="M7 0a7 7 0 0 0-7 7c0 5 7 11 7 11s7-6 7-11a7 7 0 0 0-7-7zm0 9.5A2.5 2.5 0 1 1 7 4.5a2.5 2.5 0 0 1 0 5z" fill="#fff"/></svg></span><span>Amber Crest Vending Services<br>Coral Harbor</span></div>
  <div class="contact-row" style="top:218px"><span class="ic"><svg width="16" height="16" viewBox="0 0 16 16"><path d="M3.5 1l2.5 3-1.5 2a9 9 0 0 0 5 5l2-1.5 3 2.5-1.5 2.5C6 15 1 10 1 2.5z" fill="#fff"/></svg></span><span style="line-height:34px">+1 305 555 0142</span></div>
  <div class="contact-row" style="top:288px"><span class="ic"><svg width="16" height="12" viewBox="0 0 16 12"><rect width="16" height="12" rx="1" fill="#fff"/><path d="M0 1l8 6 8-6" stroke="#0a72e6" stroke-width="1.4" fill="none"/></svg></span><span style="line-height:34px">info@ambercrestvending.com</span></div>

  <div class="f-head" style="left:972px">Quick Links</div>
  <ul class="links abs">
    <li><svg width="12" height="12" viewBox="0 0 12 12"><path d="M1 6h9M6 2l4 4-4 4" stroke="#fff" stroke-width="1.8" fill="none"/></svg>Home</li>
    <li><svg width="12" height="12" viewBox="0 0 12 12"><path d="M1 6h9M6 2l4 4-4 4" stroke="#fff" stroke-width="1.8" fill="none"/></svg>About</li>
    <li><svg width="12" height="12" viewBox="0 0 12 12"><path d="M1 6h9M6 2l4 4-4 4" stroke="#fff" stroke-width="1.8" fill="none"/></svg>Categories</li>
    <li><svg width="12" height="12" viewBox="0 0 12 12"><path d="M1 6h9M6 2l4 4-4 4" stroke="#fff" stroke-width="1.8" fill="none"/></svg>Testimonials</li>
    <li><svg width="12" height="12" viewBox="0 0 12 12"><path d="M1 6h9M6 2l4 4-4 4" stroke="#fff" stroke-width="1.8" fill="none"/></svg>Contact Us</li>
  </ul>

  <div class="f-rule abs"></div>
  <div class="copy abs center">Copyrights@2023.Amber Crest Vending Services.All Rights Reserved</div>
</footer>

</body>
</html>
```